We need a poster design for "KEVO Sports Night" events. The events have been around for 3 years and we hope the poster will give a sense of vibrant and active designs. It is more to a community event with teamwork and fun.

I have uploaded a past event poster just FYI.

Target Market(s)

Community, Family

Industry/Entity Type

Non Profit

Logo Text

KEVO Sports Night

Requirements
Must have
• KEVO Sports Night
• Organiser: KEVO Sydney
• Date: 25/11/2017
• Time: 4:00pm
• Venue: Wendamere Park
• Facebook: kevosport

```html
<!DOCTYPE html>
<html lang="en">
<head>
<meta charset="utf-8">
<title>KEVO Sports Night</title>
<link href="https://fonts.googleapis.com/css2?family=Barlow+Condensed:ital,wght@1,600;1,700;1,900&display=swap" rel="stylesheet">
<style>
  :root {
    --page: #ffffff;
    --red: #e8202a;
    --red-dark: #c0272d;
    --charcoal: #2d2a2a;
    --ember: #d9481f;
    --flame: #f07a2a;
    --ink: #1a1414;
  }
  html, body {
    margin: 0;
    width: 1200px;
    height: 1200px;
    overflow: hidden;
    background: var(--page);
  }
  .poster {
    position: absolute;
    left: 234px;
    top: 109px;
    width: 688px;
    height: 977px;
    background: var(--page);
    box-shadow: 3px 3px 4px rgba(0,0,0,0.45);
    outline: 1px solid #d8d8d8;
    font-family: "Barlow Condensed", "Arial Narrow", sans-serif;
    font-style: italic;
  }
  .photo-band {
    position: absolute;
  }
  .photo-band--left {
    left: 4px;
    top: 2px;
    width: 208px;
    height: 979px;
    background:
      radial-gradient(ellipse at 90% 22%, rgba(240,122,42,0.55), transparent 18%),
      linear-gradient(180deg, var(--charcoal) 0%, #2a2424 45%, #5a2a1e 72%, var(--ember) 100%);
  }
  .photo-band--right {
    right: -2px;
    top: 499px;
    width: 100px;
    height: 478px;
    background:
      radial-gradient(ellipse at 40% 30%, rgba(240,122,42,0.8), transparent 45%),
      linear-gradient(180deg, #3a1d16 0%, var(--ember) 35%, #a83a22 70%, var(--charcoal) 100%);
  }
  .brand {
    position: absolute;
    left: 240px;
    top: 138px;
    width: 300px;
    margin: 0;
    text-align: center;
    color: var(--red);
    font-weight: 900;
    font-size: 168px;
    line-height: 1;
    letter-spacing: -2px;
  }
  .event-title {
    position: absolute;
    left: 110px;
    top: 268px;
    width: 560px;
    margin: 0;
    text-align: center;
    font-weight: 900;
    font-size: 218px;
    line-height: 0.72;
    letter-spacing: -6px;
    background: linear-gradient(160deg, #1c1414 0%, #5a1a14 25%, var(--ember) 45%, var(--flame) 55%, #8a1e16 72%, var(--ink) 100%);
    -webkit-background-clip: text;
    background-clip: text;
    color: transparent;
    filter: drop-shadow(3px 4px 3px rgba(0,0,0,0.4));
  }
  .event-title span { display: block; }
  .details {
    position: absolute;
    left: 300px;
    top: 728px;
    width: 240px;
    text-align: center;
    color: var(--red-dark);
    font-weight: 700;
  }
  .details p { margin: 0; line-height: 34px; }
  .details .label { font-size: 18px; }
  .details .value { font-size: 32px; font-weight: 700; }
  .organiser { margin-top: 6px !important; }
  .organiser .label { font-size: 11px; line-height: 14px; display: block; }
  .organiser .value { font-size: 27px; line-height: 28px; }
  .social {
    margin-top: 16px;
    display: flex;
    align-items: center;
    justify-content: center;
    gap: 6px;
    color: var(--ink);
    font-size: 12px;
    font-weight: 700;
  }
  .social .mark {
    width: 22px;
    height: 22px;
    background: var(--ink);
  }
</style>
</head>
<body>
  <main class="poster">
    <div class="photo-band photo-band--left" role="img" aria-label="Dark action photo of a cyclist in an orange jersey with fiery smoke"></div>
    <div class="photo-band photo-band--right" role="img" aria-label="Fiery photo of a shouting athlete and a female boxer in red gloves"></div>

    <h1 class="brand">KEVO</h1>
    <h2 class="event-title"><span>SPORTS</span><span>NIGHT</span></h2>

    <section class="details">
      <p><span class="label">Date: </span><span class="value">25/11/2017</span></p>
      <p><span class="label">Time: </span><span class="value">4:00pm</span></p>
      <p><span class="label">Venue: </span><span class="value">Wendamere Park</span></p>
      <p class="organiser"><span class="label">Organised by:</span><span class="value">KEVO Sydney</span></p>
      <div class="social"><span class="mark"></span><span>kevosport</span></div>
    </section>
  </main>
</body>
</html>
```